Post Card to Promote Apartment Building

My specialty is selling apartment buildings. So, the tag line or headline should be "Tom Halvorsen Sells Apartment Buildings"

The goal is to drive traffic to the web site, where the customer can find more details about the property, including cash flow information, rent roll, and photographs of the inside and outside of the property. the web site is www.TomHalvorsen.example. The goal is to get them to go to the website or call me. my phone number is 555-318-2907. they can text to this number also. My customers are typically older, conservative, high net worth investors. So, the post card needs to be clean, professional, and classy.

The two buildings on this post card are

617 Garnet St - Store + 3 Apartments, Price $395,000, 12% return on investment. Totally renovated and fully leased with tenants paying all utilities.
482 E. Pellham St. - 2 Stores + 2 Apartments, Price $495,000, 11% return on investment. Totally renovated and fully leased with tenants paying all utilities. Located in Upper Commerce District / Exchange Square.

Call Tom Halvorsen III at 555-318-2907 or visit www.TomHalvorsen.example for more details, including cash flow details and photos of the inside and outside.

```html
<!DOCTYPE html>
<html lang="en">
<head>
<meta charset="utf-8">
<title>Tom Halvorsen Realty – Apartment Building Postcard</title>
<link rel="stylesheet" href="https://fonts.googleapis.com/css2?family=Oswald:wght@400;500;600&family=Open+Sans:wght@400;600;700&display=swap">
<style>
  :root {
    --red: #cc1e35;
    --red-dark: #a8152a;
    --brown: #4f2e1f;
    --white: #ffffff;
    --ink: #3a3a3a;
    --page: #e9e7e4;
    --stamp: #d4d4d4;
    --photo-sky: #b9c6d3;
    --photo-brick: #8b4a3a;
    --photo-green: #6d7a4a;
  }
  * { box-sizing: border-box; margin: 0; padding: 0; }
  html, body { width: 900px; height: 1200px; overflow: hidden; }
  body {
    background: var(--page);
    font-family: "Open Sans", Arial, sans-serif;
    color: var(--ink);
    position: relative;
  }
  .postcard {
    position: absolute;
    left: 60px;
    width: 780px;
    height: 510px;
    background: var(--white);
    overflow: hidden;
    box-shadow: 0 6px 18px rgba(0,0,0,0.25);
  }
  .postcard--front { top: 55px; }
  .postcard--back { top: 630px; }
  .abs { position: absolute; }

  /* Front */
  .front-header { left: 0; top: 0; width: 780px; height: 122px; background: var(--red); }
  .for-sale-tag {
    background: var(--brown);
    color: var(--white);
    font-family: "Oswald", Arial, sans-serif;
    font-weight: 600;
    text-align: center;
    line-height: 1;
  }
  .front-tag {
    left: 28px; top: 0; width: 104px; height: 158px;
    clip-path: polygon(0 0, 100% 0, 100% 100%, 50% 86%, 0 100%);
    padding-top: 26px;
    font-size: 40px;
    z-index: 3;
  }
  .front-tag .tag-for {
    display: inline-block; background: var(--white); color: var(--brown);
    padding: 2px 10px; margin-bottom: 8px;
  }
  .headline-name {
    left: 160px; top: 14px;
    font-family: "Oswald", Arial, sans-serif; font-weight: 500;
    font-size: 54px; color: var(--white); letter-spacing: 1px; line-height: 1;
  }
  .headline-tag {
    left: 160px; top: 78px;
    border: 2px solid var(--white);
    padding: 3px 14px;
    font-family: "Oswald", Arial, sans-serif; font-weight: 400;
    font-size: 24px; color: var(--white); letter-spacing: 1px; line-height: 1.1;
  }
  .front-photo {
    left: 0; top: 122px; width: 780px; height: 210px;
    background: linear-gradient(180deg, var(--photo-sky) 0%, #a99a8c 35%, var(--photo-brick) 60%, var(--photo-green) 100%);
  }
  .front-offer {
    left: 0; top: 318px; width: 420px; height: 154px;
    background: var(--red);
    clip-path: polygon(0 0, 92% 0, 100% 100%, 0 100%);
    color: var(--white);
    padding: 10px 0 0 22px;
  }
  .price {
    font-family: "Oswald", Arial, sans-serif; font-weight: 500;
    font-size: 30px; line-height: 1.1;
  }
  .feature-list { list-style: none; font-size: 13px; line-height: 1.45; }
  .feature-list li::before { content: "• "; }
  .front-brand { left: 470px; top: 352px; }
  .brand-row { display: flex; align-items: center; gap: 9px; }
  .brand-square {
    width: 38px; height: 38px; border: 3px solid var(--brown); flex: none;
  }
  .brand-name {
    font-family: "Oswald", Arial, sans-serif; font-weight: 500;
    font-size: 22px; color: var(--brown); letter-spacing: 1px; line-height: 1;
    white-space: nowrap;
  }
  .brand-line {
    font-size: 9px; font-weight: 600; color: var(--brown);
    letter-spacing: 0.3px; margin-top: 4px; text-transform: uppercase;
    white-space: nowrap;
  }
  .website-box {
    left: 440px; top: 420px; width: 315px; height: 36px;
    border: 2px solid var(--brown); border-radius: 18px;
    font-size: 15px; color: var(--brown);
    display: flex; align-items: center; justify-content: center;
  }
  .card-footer { left: 0; bottom: 0; width: 780px; height: 38px; background: var(--brown); }
  .front-footer-accent {
    left: 0; bottom: 38px; width: 780px; height: 4px; background: var(--red-dark);
  }

  /* Back */
  .back-photo {
    left: 0; top: 0; width: 520px; height: 210px;
    background: linear-gradient(160deg, #9fb0c0 0%, #7d8a96 30%, var(--photo-brick) 62%, #5e3a2e 100%);
    clip-path: polygon(0 0, 100% 0, 82% 100%, 0 78%);
  }
  .back-stripe { left: 0; top: 0; width: 780px; height: 240px; }
  .stamp-box { left: 640px; top: 28px; width: 92px; height: 96px; background: var(--stamp); }
  .back-offer { left: 22px; top: 196px; width: 380px; color: var(--ink); }
  .back-offer .price { color: var(--red); }
  .back-offer .feature-list { font-size: 10.5px; line-height: 1.45; white-space: nowrap; }
  .back-tag {
    left: 412px; top: 222px; width: 100px; height: 96px;
    font-size: 34px; padding-top: 10px;
    clip-path: polygon(0 0, 100% 12%, 100% 100%, 0 100%);
  }
  .back-tag span { display: block; }
  .contact-panel {
    left: 0; top: 330px; width: 470px; height: 142px;
    background: var(--red);
    clip-path: polygon(0 0, 96% 0, 100% 100%, 0 100%);
  }
  .headshot {
    left: 22px; top: 342px; width: 90px; height: 116px;
    background: linear-gradient(180deg, #c9ccd2 0%, #8a8f9a 60%, #3d4250 100%);
    border: 2px solid var(--white);
  }
  .contact-text { left: 132px; top: 340px; color: var(--white); }
  .contact-name {
    font-family: "Oswald", Arial, sans-serif; font-weight: 500;
    font-size: 28px; line-height: 1.15;
  }
  .contact-line { font-size: 14px; line-height: 1.45; }
  .contact-more { font-size: 14px; font-style: italic; line-height: 1.3; margin-top: 4px; }
  .back-brand { left: 486px; top: 410px; }
</style>
</head>
<body>

<section class="postcard postcard--front" aria-label="Postcard front">
  <div class="abs front-header"></div>
  <div class="abs for-sale-tag front-tag"><span class="tag-for">FOR</span><br>SALE</div>
  <h1 class="abs headline-name">TOM HALVORSEN</h1>
  <p class="abs headline-tag">SELLS APARTMENT BUILDINGS</p>
  <div class="abs front-photo" role="img" aria-label="Street photograph of the brick row building at 617 Garnet St"></div>
  <div class="abs front-offer">
    <p class="price">$395,000</p>
    <ul class="feature-list">
      <li>617 Garnet St - Store + 3 Apartments</li>
      <li>12% return on investment</li>
      <li>Totally renovated</li>
      <li>Fully leased with tenants paying all utilities</li>
    </ul>
  </div>
  <div class="abs front-brand">
    <div class="brand-row">
      <div class="brand-square"></div>
      <div>
        <p class="brand-name">TOM HALVORSEN REALTY</p>
        <p class="brand-line">Harborton's Apartment Property Specialist</p>
      </div>
    </div>
  </div>
  <p class="abs website-box">Our website - www.TomHalvorsen.example</p>
  <div class="abs front-footer-accent"></div>
  <div class="abs card-footer"></div>
</section>

<section class="postcard postcard--back" aria-label="Postcard back">
  <div class="abs back-photo" role="img" aria-label="Street photograph of the building at 482 E. Pellham St."></div>
  <svg class="abs back-stripe" width="780" height="240" viewBox="0 0 780 240" aria-hidden="true">
    <polygon points="0,164 0,176 426,214 434,210" fill="var(--red)"/>
    <polygon points="430,210 520,0 532,0 442,210" fill="var(--red)"/>
  </svg>
  <div class="abs stamp-box"></div>
  <div class="abs back-offer">
    <p class="price">$495,000</p>
    <ul class="feature-list">
      <li>482 E. Pellham St. - 2 Stores + 2 Apartments</li>
      <li>11% return on investment</li>
      <li>Totally renovated &amp; fully leased with tenants paying all utilities</li>
      <li>Located in Upper Commerce District / Exchange Square</li>
    </ul>
  </div>
  <div class="abs for-sale-tag back-tag"><span>FOR</span><span>SALE</span></div>
  <div class="abs contact-panel"></div>
  <div class="abs headshot" role="img" aria-label="Portrait photograph of Tom Halvorsen III"></div>
  <div class="abs contact-text">
    <p class="contact-name">Tom Halvorsen</p>
    <p class="contact-line">Call 555-318-2907</p>
    <p class="contact-line">www.TomHalvorsen.example</p>
    <p class="contact-more">for more details<br>visit our website...</p>
  </div>
  <div class="abs back-brand">
    <div class="brand-row">
      <div class="brand-square"></div>
      <div>
        <p class="brand-name">TOM HALVORSEN REALTY</p>
        <p class="brand-line">Harborton's Apartment Property Specialist</p>
      </div>
    </div>
  </div>
  <div class="abs card-footer"></div>
</section>

</body>
</html>
```